Talvoro Equity LLC

Need Professional Business cards for New Investment Fund

Target Market(s)

High Quality investors

Industry/Entity Type

Financial

Contact Information for Business Card

Phone Number +1 555 284 6190
Name Milan Dorovsky
Title Fund Manager
email md@FundTalvoro.com
Website www.FundTalvoro.com

Colors

Designer to choose colors to be used in the design.

Requirements
Must have
• Must have our Logo and all of the above. Must be made so lettering and loge can be raised

```html
<!DOCTYPE html>
<html lang="en">
<head>
<meta charset="utf-8">
<title>Talvoro Equity – Business Card</title>
<link rel="stylesheet" href="https://fonts.googleapis.com/css2?family=Bebas+Neue&family=Questrial&display=swap">
<style>
  :root {
    --page-bg: #e4e4e4;
    --card-white: #ffffff;
    --card-dark: #434e42;
    --accent-green: #1fe70f;
    --ink: #1c1c1c;
    --ink-light: #ffffff;
  }
  * { margin: 0; padding: 0; box-sizing: border-box; }
  html, body {
    width: 1200px;
    height: 1028px;
    overflow: hidden;
    background: var(--page-bg);
  }
  .canvas {
    position: relative;
    width: 1200px;
    height: 1028px;
  }
  .card {
    position: absolute;
    left: 310px;
    width: 579px;
    height: 331px;
    border-radius: 24px;
    overflow: hidden;
  }
  .card--front { top: 165px; background: var(--card-white); }
  .card--back { top: 532px; background: var(--card-dark); }

  .identity {
    position: absolute;
    right: calc(579px - 262px);
    top: 134px;
    text-align: right;
  }
  .identity__name {
    font-family: "Bebas Neue", sans-serif;
    font-size: 39px;
    line-height: 1;
    color: var(--accent-green);
    letter-spacing: 0.2px;
    white-space: nowrap;
  }
  .identity__title {
    font-family: "Questrial", sans-serif;
    font-size: 17px;
    line-height: 1;
    color: var(--ink);
    margin-top: 4px;
  }
  .divider {
    position: absolute;
    left: 291px;
    top: 138px;
    width: 2px;
    height: 55px;
    background: var(--accent-green);
  }
  .contacts {
    position: absolute;
    left: 320px;
    top: 133px;
    list-style: none;
    font-family: "Questrial", sans-serif;
    font-size: 17px;
    color: var(--ink);
  }
  .contacts__item {
    display: flex;
    align-items: center;
    height: 20.5px;
    white-space: nowrap;
  }
  .contacts__icon {
    width: 12px;
    height: 12px;
    margin-right: 9px;
    flex: none;
  }

  .brand {
    position: absolute;
    left: 50%;
    top: 50%;
    transform: translate(-50%, -50%);
    display: flex;
    align-items: center;
    gap: 12px;
  }
  .brand__mark {
    width: 18px;
    height: 18px;
    background: var(--accent-green);
  }
  .brand__name {
    font-family: "Questrial", sans-serif;
    font-size: 36px;
    color: var(--ink-light);
    letter-spacing: 1px;
  }
</style>
</head>
<body>
<main class="canvas">
  <section class="card card--front" aria-label="Business card front">
    <div class="identity">
      <h1 class="identity__name">MILAN DOROVSKY</h1>
      <p class="identity__title">Fund Manager</p>
    </div>
    <div class="divider"></div>
    <ul class="contacts">
      <li class="contacts__item">
        <svg class="contacts__icon" viewBox="0 0 12 12" aria-hidden="true">
          <path d="M3 1 L5 3.5 L4 5 Q5 7.5 7 8.5 L8.5 7.5 L11 9.5 L9.5 11 Q4 10 1.5 3 Z" fill="none" stroke="var(--accent-green)" stroke-width="1.1" stroke-linejoin="round"/>
        </svg>
        +1 555 284 6190
      </li>
      <li class="contacts__item">
        <svg class="contacts__icon" viewBox="0 0 12 12" aria-hidden="true">
          <rect x="1" y="2.5" width="10" height="7" fill="none" stroke="var(--accent-green)" stroke-width="1.1"/>
          <path d="M1 2.5 L6 6.5 L11 2.5" fill="none" stroke="var(--accent-green)" stroke-width="1.1"/>
        </svg>
        md@FundTalvoro.com
      </li>
      <li class="contacts__item">
        <svg class="contacts__icon" viewBox="0 0 12 12" aria-hidden="true">
          <circle cx="6" cy="6" r="5" fill="none" stroke="var(--accent-green)" stroke-width="1.1"/>
          <ellipse cx="6" cy="6" rx="2.2" ry="5" fill="none" stroke="var(--accent-green)" stroke-width="1"/>
          <path d="M1 6 H11 M2 3.5 H10 M2 8.5 H10" stroke="var(--accent-green)" stroke-width="1"/>
        </svg>
        www.FundTalvoro.com
      </li>
    </ul>
  </section>

  <section class="card card--back" aria-label="Business card back">
    <div class="brand">
      <span class="brand__mark"></span>
      <span class="brand__name">Talvoro</span>
    </div>
  </section>
</main>
</body>
</html>
```